A professional I.T consulting company requires a web design

Our company needs a fresh web design to help us drive our business forward. We are an Information Technology company who specialises in solutions based I.T delivery and consultations and who prides ourselves on our professional approach to business.

We would like a web site design from a designer who may be able to help us upload the site to WordPress and who may be interested in completing the "coding" section of the site (minimal coding). Although this is not essential to this project and won't factor into the decision making process.

A very thorough brief has been put together for this design project so very limited work is required in regards to content (the brief sets out all the content text - copy write material).

Please see the attached project documents for a copy of the brief

Target Market(s)

Please refer to the attached brief

Industry/Entity Type

Business

Requirements
Must have
• Please refer to the attached brief
Nice to have
Should not have

```html
<!DOCTYPE html>
<html lang="en">
<head>
<meta charset="utf-8">
<title>KORVEX – IT Solutions</title>
<link href="https://fonts.googleapis.com/css2?family=Exo+2:wght@300;400;600;700&family=Arimo:wght@400;700&display=swap" rel="stylesheet">
<style>
:root{
  --blue:#1f8fd6;
  --blue-dark:#1570b3;
  --blue-light:#3aa8e6;
  --ink:#222;
  --text:#333;
  --muted:#666;
  --grey-bg:#ececec;
  --card-bg:#f7f7f7;
  --line:#dedede;
  --nav-dark:#14222e;
  --footer:#0b0b0b;
  --white:#fff;
}
*{box-sizing:border-box;margin:0;padding:0}
html,body{width:790px;height:1200px;overflow:hidden}
body{font-family:"Arimo",Arial,sans-serif;color:var(--text);background:var(--white);position:relative}
.abs{position:absolute}

/* header */
.site-header{position:absolute;left:0;top:0;width:790px;height:82px}
.brand{left:66px;top:18px;height:48px;display:flex;align-items:center;gap:8px}
.brand-mark{width:46px;height:46px;border-radius:50%;background:var(--blue)}
.brand-name{font-family:"Exo 2",sans-serif;font-weight:700;font-size:30px;color:var(--blue);letter-spacing:1px;line-height:1}
.phone{left:430px;top:34px;font-size:13px;color:#444;display:flex;align-items:center;gap:8px}
.search{left:565px;top:28px;width:160px;height:30px;border-radius:5px;background:var(--blue);padding:3px;display:flex}
.search-field{flex:1;background:#f4f4f4;border-radius:3px;font-size:8px;color:#999;padding:9px 8px 0}
.search-btn{width:26px;display:flex;align-items:center;justify-content:center}

/* nav */
.main-nav{position:absolute;left:0;top:82px;width:790px;height:35px;background:linear-gradient(var(--blue-light),var(--blue-dark));display:flex;padding-left:66px}
.main-nav a{color:var(--white);text-decoration:none;font-size:11px;line-height:35px;padding:0 14px}
.main-nav a.active{background:var(--nav-dark);padding:0 18px}

/* hero */
.hero{position:absolute;left:0;top:117px;width:790px;height:324px}
.hero-photo{position:absolute;inset:0;background:linear-gradient(90deg,#e6e8ea 0%,#c9ccce 35%,#6b6f72 62%,#3b3e41 100%)}
.hero-title{left:66px;top:128px;width:324px;height:40px;background:var(--blue);color:var(--white);font-family:"Exo 2",sans-serif;font-size:20px;padding:7px 14px}
.hero-sub{left:66px;top:168px;width:354px;height:46px;background:rgba(70,70,70,.85);color:#eee;font-size:11.5px;line-height:15px;padding:8px 14px}
.hero-arrow{top:159px;width:24px;height:24px;border-radius:50%;background:#f2f2f2;border:3px solid rgba(0,0,0,.25);display:flex;align-items:center;justify-content:center}

/* features */
.feature{position:absolute;top:462px;width:210px;height:232px;background:var(--card-bg);border:1px solid #e4e4e4;text-align:center}
.feature-icon{width:90px;height:90px;border-radius:50%;background:var(--blue);border:3px solid #dfe9f2;margin:14px auto 0;display:flex;align-items:center;justify-content:center}
.feature-shadow{width:70px;height:4px;border-radius:50%;background:#cfcfcf;margin:6px auto 0}
.feature h3{font-family:"Exo 2",sans-serif;font-weight:400;font-size:15px;color:var(--ink);margin-top:10px}
.feature p{font-size:7.4px;line-height:14.4px;color:#444;margin:6px 12px 0}
.btn{display:inline-block;background:var(--blue);color:var(--white);font-size:8px;font-weight:700;padding:8px 9px;border-radius:2px;margin-top:11px}

/* news + welcome */
.info{position:absolute;left:0;top:726px;width:790px;height:264px;background:var(--grey-bg)}
.info h2{position:absolute;top:11px;font-family:"Exo 2",sans-serif;font-weight:400;font-size:15px;color:var(--ink)}
.info-rule{position:absolute;left:0;top:36px;width:790px;height:1px;background:#dcdcdc}
.news{position:absolute;left:66px;width:356px;height:100px}
.news-date{position:absolute;left:0;top:0;width:36px;height:36px;background:var(--white);border:1px solid #ddd;font-size:16px;text-align:center;line-height:34px;color:var(--ink)}
.news-month{position:absolute;left:9px;top:47px;font-size:11px;color:#333}
.news-title{position:absolute;left:55px;top:2px;font-size:9px;color:#333}
.news-meta{position:absolute;left:55px;top:21px;font-size:7px;color:#333;display:flex;align-items:center;gap:6px}
.news-meta i{width:8px;height:6px;background:#777;display:block}
.news-body{position:absolute;left:55px;top:43px;width:300px;font-size:7.3px;line-height:14.4px;color:#444;text-align:justify}
.news-more{color:var(--blue)}
.welcome-photo{left:458px;top:56px;width:267px;height:95px;border:3px solid var(--white);background:linear-gradient(180deg,#8d9298 0%,#b8c4cc 50%,#3f86b8 100%)}
.welcome-text{left:457px;top:164px;width:268px;font-size:7.3px;line-height:14.4px;color:#444;text-align:justify}
.welcome-more{left:674px;top:236px;width:48px;height:16px;background:var(--blue);color:var(--white);font-size:7.5px;text-align:center;line-height:16px}

/* partners */
.partners{position:absolute;left:66px;top:1000px;width:660px;height:80px;display:flex;justify-content:space-between;align-items:center}
.partners span{font-family:"Exo 2",sans-serif;font-weight:700;font-size:24px;color:#1d3f8f}
.partners span.dark{color:#3a3a3a}

/* support band */
.support{position:absolute;left:0;top:1090px;width:790px;height:47px;background:var(--blue-light);display:flex;align-items:center;padding-left:85px}
.support-item{display:flex;align-items:center;gap:7px;color:var(--white);font-family:"Exo 2",sans-serif;font-size:13px;width:175px}
.support-item .dot{width:16px;height:16px;border-radius:3px;background:rgba(255,255,255,.9)}

/* footer */
.site-footer{position:absolute;left:0;top:1137px;width:790px;height:63px;background:var(--footer);color:#ccc}
.footer-links{left:71px;top:19px;font-size:7.5px}
.footer-copy{left:71px;top:44px;font-size:7px;color:#999}
.social{left:582px;top:20px;display:flex;gap:11px}
.social i{width:20px;height:20px;border-radius:50%;background:#d9d9d9;display:block}
</style>
</head>
<body>

<header class="site-header">
  <div class="abs brand">
    <div class="brand-mark"></div>
    <div class="brand-name">KORVEX</div>
  </div>
  <div class="abs phone">
    <svg width="10" height="12" viewBox="0 0 10 12"><path d="M2 0l2 3-1 1.5c.6 1.6 1.8 3 3.3 3.8L7.5 7 10 9l-1 2.5C4.5 11 .5 6.5 0 1.5z" fill="#333"/></svg>
    (+01) 555 204 8817
  </div>
  <div class="abs search">
    <div class="search-field">SEARCH</div>
    <div class="search-btn"><svg width="12" height="12" viewBox="0 0 12 12"><circle cx="5" cy="5" r="3.5" stroke="#fff" stroke-width="1.6" fill="none"/><path d="M7.5 7.5L11 11" stroke="#fff" stroke-width="1.8"/></svg></div>
  </div>
</header>

<nav class="main-nav">
  <a class="active">Home</a><a>About Us</a><a>Why KORVEX?</a><a>Services</a><a>Solutions</a><a>Technologies</a><a>Contact Us</a>
</nav>

<section class="hero">
  <div class="hero-photo" role="img" aria-label="Business professional holding a phone beside a server room with floating technology cubes"></div>
  <div class="abs hero-title">We succeed, when you succeed.</div>
  <div class="abs hero-sub">Our business is simple, provide you best solutions and support possible to achieve your goals</div>
  <div class="abs hero-arrow" style="left:18px"><svg width="8" height="8" viewBox="0 0 8 8"><path d="M5 1L2 4l3 3" stroke="#555" stroke-width="1.4" fill="none"/></svg></div>
  <div class="abs hero-arrow" style="left:741px"><svg width="8" height="8" viewBox="0 0 8 8"><path d="M3 1l3 3-3 3" stroke="#555" stroke-width="1.4" fill="none"/></svg></div>
</section>

<article class="feature" style="left:66px">
  <div class="feature-icon"><svg width="48" height="48" viewBox="0 0 48 48" fill="#fff"><circle cx="18" cy="18" r="10"/><circle cx="36" cy="14" r="6"/><circle cx="24" cy="36" r="7"/><circle cx="18" cy="18" r="4" fill="#1f8fd6"/><circle cx="36" cy="14" r="2.5" fill="#1f8fd6"/><circle cx="24" cy="36" r="3" fill="#1f8fd6"/></svg></div>
  <div class="feature-shadow"></div>
  <h3>Services</h3>
  <p>Lorem ipsum dolor sit amet, consectetur adipiscing elit. Vivamus mollis dignissim lacus eu posuere. Nullam viverra accumsan dui eleifend condimentum. Phasellus quam nulla lipsumu dolor.</p>
  <span class="btn">Read More</span>
</article>
<article class="feature" style="left:290px">
  <div class="feature-icon"><svg width="40" height="50" viewBox="0 0 40 50" fill="#fff"><path d="M20 2a16 16 0 0 0-9 29v6h18v-6A16 16 0 0 0 20 2z"/><rect x="11" y="40" width="18" height="3"/><rect x="13" y="45" width="14" height="3"/><path d="M20 10l-8 9h5v12h6V19h5z" fill="#1f8fd6"/></svg></div>
  <div class="feature-shadow"></div>
  <h3>Solutions</h3>
  <p>Lorem ipsum dolor sit amet, consectetur adipiscing elit. Vivamus mollis dignissim lacus eu posuere. Nullam viverra accumsan dui eleifend condimentum. Phasellus quam nulla lipsumu dolor.</p>
  <span class="btn">Read More</span>
</article>
<article class="feature" style="left:514px">
  <div class="feature-icon"><svg width="52" height="52" viewBox="0 0 52 52"><circle cx="26" cy="26" r="22" fill="#fff"/><circle cx="26" cy="26" r="15" fill="#1f8fd6"/><path d="M18 18c4-3 9-2 10 1s-3 4-2 8-6 6-8 3-3-9 0-12zM31 30c3-1 5 1 4 4s-4 3-5 1 0-4 1-5z" fill="#fff"/></svg></div>
  <div class="feature-shadow"></div>
  <h3>Technologies</h3>
  <p>Lorem ipsum dolor sit amet, consectetur adipiscing elit. Vivamus mollis dignissim lacus eu posuere. Nullam viverra accumsan dui eleifend condimentum. Phasellus quam nulla lipsumu dolor.</p>
  <span class="btn">Read More</span>
</article>

<section class="info">
  <h2 style="left:66px">Latest News</h2>
  <h2 style="left:457px">Welcome to KORVEX</h2>
  <div class="info-rule"></div>

  <div class="news" style="top:56px">
    <div class="news-date">19</div><div class="news-month">May</div>
    <div class="news-title">Lipsum is Simply Dummy Text</div>
    <div class="news-meta"><i></i>11 Comments</div>
    <div class="news-body">Lorem Ipsum is simply dummy text of the printing and typesetting industry. Lorem Ipsum has been the industry. it to make a type specimen book. It has survived into electronic typesetting Graphic Design Power of all web design. <span style="float:right" class="news-more">Read More</span></div>
  </div>
  <div class="news" style="top:162px">
    <div class="news-date">20</div><div class="news-month">May</div>
    <div class="news-title">Lipsum is Simply Dummy Text</div>
    <div class="news-meta"><i></i>21 Comments</div>
    <div class="news-body">Lorem Ipsum is simply dummy text of the printing and typesetting industry. Lorem Ipsum has been the industry. it to make a type specimen book. It has survived into electronic typesetting Graphic Design Power of all web design. <span style="float:right" class="news-more">Read More</span></div>
  </div>

  <div class="abs welcome-photo" role="img" aria-label="Tablet showing a world map with location pins and floating bubbles labelled team work, mentor and motivate"></div>
  <p class="abs welcome-text">KORVEX provides quality Information Technology support and solutions services for businesses throughout the Riverbend Valley and the greater Metropolitan areas. We pride ourselves on our professional approach to our service delivery and in our no-nonsense approach to meeting our client's unique business I.T needs.</p>
  <div class="abs welcome-more">More</div>
</section>

<div class="partners">
  <span class="dark">NORTIX</span>
  <span>DALVO</span>
  <span>HELPRA</span>
  <span>ORBIN</span>
  <span>QUESTA</span>
</div>

<div class="support">
  <div class="support-item"><svg width="16" height="16" viewBox="0 0 16 16"><path d="M2 2l12 12M14 2L2 14" stroke="#fff" stroke-width="2.4"/></svg>Log Service</div>
  <div class="support-item"><svg width="16" height="16" viewBox="0 0 16 16"><path d="M3 1l3 4-1.5 2c1 2 2.5 3.5 4.5 4.5L11 10l4 3-1.5 3C7 15 1 9 1 2.5z" fill="#fff"/></svg>Call 1300 555 019</div>
  <div class="support-item" style="width:187px"><span class="dot"></span>Desktop Support</div>
  <div class="support-item"><span class="dot"></span>Laptop Support</div>
</div>

<footer class="site-footer">
  <div class="abs footer-links">Site Map &nbsp;|&nbsp; Privacy Policy &nbsp;|&nbsp; Terms &amp; Condition &nbsp;|&nbsp; Contact Us</div>
  <div class="abs footer-copy">© 2014 KORVEX. All Rights Reserved</div>
  <div class="abs social"><i></i><i></i><i></i><i></i><i></i></div>
</footer>

</body>
</html>
```